Packaging design for Virgin Coconut Oil. 100% pure cold pressed coconut oil

We need a new packaging and label design for our Virgin Coconut Oil product. It is currently marketed in the Philippines as a food supplement. We would like to try marketing it to other Asian countries such as Singapore, Malaysia and Hong Kong. The company has been producing this product since 2004 but now would like to venture into exporting our products overseas.

Would like to see designs with earth, natural "organic" colors. Fresh, Clean and pure look. Our trade mark is "Kestrel Meadow". Its a 100% pure cold pressed virgin coconut oil. All in all, we want to totally repackage our product and re-design the trademark to cater to export markets. Thanks!

Mid to High

Health Product

cadf82
9bcb3b
33b8a4
ffffff
3176b5
3276b5
0592cd
fbed22
fece3e

• Bottle shape design ideas.

```html
<!DOCTYPE html>
<html lang="en">
<head>
<meta charset="utf-8">
<title>Kestrel Meadow Virgin Coconut Oil Label</title>
<link rel="stylesheet" href="https://fonts.googleapis.com/css2?family=Bebas+Neue&family=Roboto+Condensed:wght@500;600&display=swap">
<style>
  :root {
    --backdrop: #f1f1ef;
    --label: #ffffff;
    --brand: #e98a4b;
    --approved: #8b3a1f;
    --approved-rule: #d08a5c;
    --pure: #7467a6;
    --pure-rule: #8f84bd;
    --natural: #2f6d2b;
    --natural-rule: #4f8a3c;
    --ink: #2b2b2b;
    --palm-a: #1f9a57;
    --palm-b: #58c08f;
    --nut-a: #a5532d;
    --nut-b: #e0a36e;
  }
  * { margin: 0; padding: 0; box-sizing: border-box; }
  html, body {
    width: 1200px;
    height: 1111px;
    overflow: hidden;
    background: var(--backdrop);
  }
  .label {
    position: absolute;
    left: 359px;
    top: 55px;
    width: 482px;
    height: 1000px;
    background: var(--label);
    box-shadow: 0 6px 24px rgba(0,0,0,0.08);
    overflow: hidden;
  }
  .brand-name {
    position: absolute;
    left: 60px;
    top: 132px;
    height: 752px;
    width: 130px;
    writing-mode: vertical-rl;
    transform: rotate(180deg);
    font-family: "Bebas Neue", "Oswald", sans-serif;
    font-size: 138px;
    line-height: 130px;
    letter-spacing: 1px;
    color: var(--brand);
    text-align: center;
    white-space: nowrap;
  }
  .palm-fronds {
    position: absolute;
    left: 270px;
    top: 0;
    width: 212px;
    height: 411px;
    border-bottom-left-radius: 70% 60%;
    background: linear-gradient(200deg, var(--palm-b) 0%, var(--palm-a) 60%, rgba(31,154,87,0.15) 100%);
    opacity: 0.85;
  }
  .coconut {
    position: absolute;
    left: 196px;
    top: 372px;
    width: 252px;
    height: 172px;
    border-radius: 50%;
    background: radial-gradient(ellipse at 40% 45%, var(--nut-b) 0%, var(--nut-a) 70%, rgba(165,83,45,0) 100%);
  }
  .claims {
    position: absolute;
    left: 215px;
    top: 580px;
    right: 0;
    font-family: "Roboto Condensed", "Arial Narrow", sans-serif;
    font-weight: 600;
    text-transform: uppercase;
  }
  .claim {
    border-bottom: 3px solid;
  }
  .claim-approved {
    color: var(--approved);
    border-color: var(--approved-rule);
    font-size: 19px;
    line-height: 25px;
    padding-bottom: 10px;
  }
  .claim-pure {
    color: var(--pure);
    border-color: var(--pure-rule);
    font-size: 23px;
    line-height: 28px;
    padding: 14px 0 14px;
  }
  .claim-natural {
    color: var(--natural);
    border-color: var(--natural-rule);
    font-size: 28px;
    line-height: 35px;
    padding: 14px 0 16px;
  }
  .since {
    margin-top: 30px;
    font-size: 20px;
    color: var(--ink);
    font-weight: 500;
    letter-spacing: 1px;
  }
  .volume {
    margin-top: 34px;
    font-size: 20px;
    color: var(--ink);
    font-weight: 500;
    letter-spacing: 1px;
  }
</style>
</head>
<body>
  <main class="label">
    <div class="palm-fronds" role="img" aria-label="Watercolour illustration of green palm fronds"></div>
    <h1 class="brand-name">Kestrel Meadow</h1>
    <div class="coconut" role="img" aria-label="Watercolour illustration of a whole and a halved coconut with leaves"></div>
    <section class="claims">
      <p class="claim claim-approved">Approved<br>Therapeutic Clean</p>
      <p class="claim claim-pure">100% Pure<br>Cold Pressed</p>
      <p class="claim claim-natural">All Natural<br>Food Supplement</p>
      <p class="since">Since 2004</p>
      <p class="volume">500ML | OZ1500</p>
    </section>
  </main>
</body>
</html>
```